Business Card Design Project

We need a business card design for a management consultancy focused on financial innovation and digital money, run by experts from the Financial Services, Telecoms and Money Transfer industries.
Our products include services such as Mobile Payments, Mobile Money, Digital Wallets, Online Payments, Branchless Banking and more. We work with regulatory information, business plans, financial modelling, strategic planning, new products functional specification, new technologies evaluation, etc.
See company logo attached.
We would like to see 2 versions: one in portuguese and one in english (regarding data information). You can see below information needed (whenever there is a difference between the two versions, the first one is in english and the second one in portuguese).

Name
Position
Phone/ Tel: ++55-11-xxxx-xxxx
Cell/ Cel: ++55-11-9 xxxx-xxxx
Dr. Tavares Lobato Av., 318 - Tower II - 16th floor / Avenida Dr. Tavares Lobato, 318 - Bloco B - 9o. andar
São Paulo - SP
01327-118 - Brazil/ 01327-118 - Brasil

Target Market(s)

Audience: C-level executives from banks, credit card companies, acquirers, IT developers, retailers

Industry/Entity Type

Financial

Requirements
Must have
• Must use the logo and information above. Front must have white background. Back side should have only logo.
Nice to have
• Back should be in another colour but if it seems too exxagerated, maintain back in white also.
Should not have
• Do not add other illustrations to the business card.

```html
<!DOCTYPE html>
<html lang="pt">
<head>
<meta charset="utf-8">
<title>Veral Management Consulting – Business Card</title>
<link href="https://fonts.googleapis.com/css2?family=Cinzel:wght@400;500&family=Open+Sans:wght@400;600&display=swap" rel="stylesheet">
<style>
  :root {
    --canvas: #e9e6e1;
    --card-white: #ffffff;
    --ink-grey: #5f6166;
    --ink-light: #8a8c91;
    --brand-blue: #4a6a98;
    --name-violet: #4b3fa8;
    --rule: #3d3f44;
    --back-deep: #0f2550;
    --back-mid: #1d4a8c;
    --back-light: #2f66ad;
    --icon-fill: #6f9fd1;
  }
  * { margin: 0; padding: 0; box-sizing: border-box; }
  html, body { width: 1200px; height: 1023px; overflow: hidden; }
  body {
    background: var(--canvas);
    position: relative;
    font-family: "Open Sans", Arial, sans-serif;
  }
  .card {
    position: absolute;
    width: 700px;
    height: 400px;
    border-radius: 4px;
    box-shadow: 0 10px 28px rgba(0,0,0,.18);
    overflow: hidden;
  }
  .card-front { left: 60px; top: 70px; background: var(--card-white); }
  .front-company { position: absolute; left: 40px; top: 34px; }
  .company-name {
    font-family: "Cinzel", Georgia, serif;
    font-size: 44px;
    letter-spacing: 2px;
    color: var(--brand-blue);
    line-height: 1;
    display: flex;
    align-items: center;
    gap: 14px;
  }
  .brand-square { width: 16px; height: 16px; background: var(--brand-blue); display: inline-block; }
  .company-tagline {
    font-family: "Cinzel", Georgia, serif;
    font-size: 19px;
    letter-spacing: 3px;
    color: var(--ink-grey);
    margin-top: 8px;
    margin-left: 30px;
  }
  .contact-block { position: absolute; right: 40px; top: 150px; width: 290px; text-align: right; }
  .person-name {
    font-family: "Cinzel", Georgia, serif;
    font-size: 26px;
    letter-spacing: 1.5px;
    color: var(--name-violet);
  }
  .person-role {
    font-size: 12px;
    letter-spacing: 2px;
    color: var(--ink-light);
    margin-bottom: 14px;
  }
  .contact-line {
    display: flex;
    justify-content: flex-end;
    align-items: center;
    gap: 10px;
    font-size: 13px;
    color: var(--ink-grey);
    line-height: 22px;
  }
  .contact-icon { width: 14px; height: 14px; flex: none; }
  .divider { position: absolute; left: 380px; right: 0; top: 288px; height: 1.5px; background: var(--rule); }
  .address-block {
    position: absolute; left: 370px; top: 302px; right: 40px;
    display: flex; gap: 14px; align-items: flex-start;
  }
  .region-map {
    width: 50px; height: 50px; border-radius: 50%;
    border: 2px solid var(--brand-blue);
    background: radial-gradient(circle, #5a86c4 0%, #24508f 70%);
    flex: none; margin-top: 6px;
  }
  .address { font-size: 13px; color: var(--ink-grey); line-height: 20px; }
  .address-line { display: flex; align-items: center; gap: 6px; }
  .card-back {
    left: 440px; top: 550px;
    background: linear-gradient(135deg, var(--back-deep) 0%, var(--back-mid) 55%, var(--back-light) 100%);
    display: flex; align-items: center; justify-content: center;
  }
  .back-lockup { text-align: center; color: #fff; }
  .back-lockup .company-name { color: #fff; font-size: 50px; justify-content: center; }
  .back-lockup .brand-square { background: #fff; }
  .back-lockup .company-tagline { color: #fff; margin-left: 0; font-size: 20px; }
</style>
</head>
<body>

<section class="card card-front" aria-label="Card front">
  <div class="front-company">
    <div class="company-name"><span class="brand-square"></span>Veral</div>
    <div class="company-tagline">Management Consulting</div>
  </div>

  <div class="contact-block">
    <div class="person-name">Marco Reis</div>
    <div class="person-role">DIRECTOR</div>
    <div class="contact-line">++55-11-xxxx-xxxx
      <svg class="contact-icon" viewBox="0 0 14 14"><circle cx="7" cy="7" r="7" fill="var(--icon-fill)"/><path d="M4.5 3.5l1.5 0 .6 1.8-1 .7a5 5 0 0 0 2.4 2.4l.7-1 1.8.6v1.5c0 .5-.5.9-1 .9A6 6 0 0 1 3.6 4.5c0-.5.4-1 .9-1z" fill="#fff"/></svg>
    </div>
    <div class="contact-line">++55-11-9 xxxx-xxxx
      <svg class="contact-icon" viewBox="0 0 14 14"><circle cx="7" cy="7" r="7" fill="var(--icon-fill)"/><rect x="4.8" y="3" width="4.4" height="8" rx="0.8" fill="#fff"/></svg>
    </div>
    <div class="contact-line">mreis@veralconsult.com
      <svg class="contact-icon" viewBox="0 0 14 14"><circle cx="7" cy="7" r="7" fill="var(--icon-fill)"/><rect x="3.5" y="4.5" width="7" height="5" fill="#fff"/><path d="M3.5 4.5L7 7.3l3.5-2.8" stroke="var(--icon-fill)" fill="none"/></svg>
    </div>
  </div>

  <div class="divider"></div>

  <div class="address-block">
    <div class="region-map" role="img" aria-label="Map of Brazil in a circle"></div>
    <div class="address">
      <div>Avenida Dr. Tavares Lobato</div>
      <div>318 - Bloco B - 9o. andar</div>
      <div>São Paulo - SP</div>
      <div class="address-line">
        <svg class="contact-icon" viewBox="0 0 14 14"><circle cx="7" cy="7" r="7" fill="var(--brand-blue)"/><path d="M7 3a2.5 2.5 0 0 0-2.5 2.5C4.5 7.5 7 11 7 11s2.5-3.5 2.5-5.5A2.5 2.5 0 0 0 7 3z" fill="#fff"/></svg>
        01327-118 - Brasil
      </div>
    </div>
  </div>
</section>

<section class="card card-back" aria-label="Card back">
  <div class="back-lockup">
    <div class="company-name"><span class="brand-square"></span>Veral</div>
    <div class="company-tagline">Management Consulting</div>
  </div>
</section>

</body>
</html>
```